Cedar Lantern Letterhead

I just need letterhead for my integrative psychiatry business. I'm going to use this to do mailings to other doctors, as well as send letters to patients. Thank you

Business

```html
<!DOCTYPE html>
<html lang="en">
<head>
<meta charset="utf-8">
<title>Cedar Lantern Letterhead</title>
<link href="https://fonts.googleapis.com/css2?family=Open+Sans:wght@400;600;700&family=Homemade+Apple&display=swap" rel="stylesheet">
<style>
  :root {
    --backdrop: #e9d3d2;
    --paper: #ffffff;
    --forest: #1f4423;
    --bark: #6b3a14;
    --ink: #3a3a3a;
    --mist: #efebe6;
  }
  * { box-sizing: border-box; margin: 0; padding: 0; }
  html, body {
    width: 1200px; height: 800px; overflow: hidden;
    background: var(--backdrop);
    font-family: "Open Sans", Arial, sans-serif;
  }
  .canvas {
    width: 1200px; height: 800px;
    display: flex; align-items: center; justify-content: center;
  }
  .letterhead {
    position: relative;
    width: 540px; height: 740px;
    background: var(--paper);
    overflow: hidden;
    box-shadow: 0 6px 24px rgba(90, 50, 50, 0.18);
    color: var(--ink);
  }
  .brand {
    position: absolute; left: 44px; top: 58px;
    display: flex; align-items: center; gap: 10px;
  }
  .brand-dot {
    width: 30px; height: 30px; border-radius: 50%;
    background: var(--forest);
  }
  .brand-name {
    font-size: 18px; font-weight: 600; color: var(--bark);
  }
  .contact {
    position: absolute; right: 44px; top: 40px;
    list-style: none;
    font-size: 9px; font-weight: 700; line-height: 1.35;
    color: var(--forest);
  }
  .watermark {
    position: absolute; left: 175px; top: 150px;
    width: 230px; height: 230px; border-radius: 50%;
    background: var(--mist);
    opacity: 0.7;
  }
  .letter {
    position: absolute; left: 44px; right: 44px; top: 170px;
    font-size: 9.6px; line-height: 1.55;
  }
  .salutation { font-size: 12px; margin-bottom: 14px; }
  .letter p.body { margin-bottom: 14px; text-align: left; }
  .signature {
    position: absolute; right: 70px; top: 470px;
    font-family: "Homemade Apple", cursive;
    font-size: 20px; color: var(--ink);
    transform: rotate(-6deg);
  }
  .signatory {
    position: absolute; left: 44px; top: 520px;
  }
  .signatory-name { font-size: 12px; font-weight: 600; }
  .signatory-role { font-size: 8.5px; margin-top: 3px; }
  .footer-wave {
    position: absolute; left: 0; bottom: 0;
    width: 540px; height: 740px;
  }
</style>
</head>
<body>
<main class="canvas">
  <article class="letterhead">
    <header>
      <div class="brand">
        <span class="brand-dot"></span>
        <span class="brand-name">Cedar Lantern</span>
      </div>
      <ul class="contact">
        <li>555-014-2210</li>
        <li>555-014-2211</li>
        <li>48 Alder Crest Lane</li>
        <li>Pine Ridge, CA 95999</li>
        <li>www.cedarlanternhealth.com</li>
      </ul>
    </header>

    <div class="watermark" role="img" aria-label="Faint brand emblem placed behind the letter text"></div>

    <section class="letter">
      <p class="salutation">Dear Mr. Smith,</p>
      <p class="body">Thank you for your continued trust in our practice. At Cedar Lantern we combine careful psychiatric assessment with nutrition, sleep, movement and mindfulness support, so that each plan reflects the whole person rather than a single diagnosis. We work closely with primary care physicians and specialists, sharing clear notes after every visit and welcoming questions at any stage. Our goal is steady, lasting progress built on respect, evidence and a calm, unhurried pace of care.</p>
      <p class="body">If you would like to refer a patient, please call our office or send a brief summary by mail. New patients are usually seen within two weeks, and we offer both in-person and secure video appointments. Please let us know of any recent medications, lab results or hospital stays so we can prepare well. We look forward to working together.</p>
    </section>

    <p class="signature">John Doe</p>
    <div class="signatory">
      <p class="signatory-name">John Doe</p>
      <p class="signatory-role">Co-Founder &amp; CEO</p>
    </div>

    <svg class="footer-wave" viewBox="0 0 540 740" aria-hidden="true">
      <path fill="var(--bark)" d="M0,722 C210,712 370,650 540,560 L540,574 C370,664 210,724 0,730 Z"/>
      <path fill="var(--forest)" d="M0,740 C220,730 380,668 540,590 L540,740 Z"/>
    </svg>
  </article>
</main>
</body>
</html>
```